Business card design needed

Our company background is that we provides transfers to and from the airport, social & corporate events, weddings.
We are also available for charter for birthday party, wine tastings, concerts, anniversary, school balls etc.
Our business cards have to reflect that we have a professional company, they are our first contact and have to stand out from the other 'players' in the market.

Industry/Entity Type

School

Contact Information for Business Card

BRISTEL QDF, Laurent & Marisol, mob: 0427 381 594, PO Box 287, Tarrowin WA 6311, ABN 52 914 603 278, Lic 7169/5804,

Requirements
Must have
• Telephone number: 0427 381 594
Website: www.BRISTELQDF.com.au
postal address: PO Box 287, Tarrowin WA 6311
Licences: Lic 7169/5804

***If using the new photo (one with the bus and buildings behind it), if possible can the buildings be cropped out. Thanks
Nice to have
• would be nice to have the pics of the vehicle(s), preferred the Pel on the card but not too fussed.
Should not have
• Picture of vehicle we don't have in our fleet. (We ONLY have the Pellics and Rendak Ovaro mini bus)

```html
<!DOCTYPE html>
<html lang="en">
<head>
<meta charset="utf-8">
<title>BRISTEL QDF – Business Card</title>
<link rel="stylesheet" href="https://fonts.googleapis.com/css2?family=Arimo:wght@400&display=swap">
<style>
  :root {
    --page-bg: #e9ecee;
    --card-charcoal: #2f2c2c;
    --band-grey: #8c8c8c;
    --swoosh-grey: #a3a3a3;
    --swoosh-white: #ffffff;
    --text-white: #ffffff;
    --photo-sky: #dfe7ee;
    --photo-trees: #4e6a3c;
    --photo-car: #b8b2a6;
    --photo-brick: #a2533a;
  }
  * { margin: 0; padding: 0; box-sizing: border-box; }
  html, body {
    width: 1200px;
    height: 960px;
    overflow: hidden;
    background: var(--page-bg);
    font-family: "Arimo", Arial, sans-serif;
  }
  .business-card {
    position: absolute;
    left: 100px;
    top: 174px;
    width: 1000px;
    height: 611px;
    overflow: hidden;
    box-shadow: 0 10px 30px rgba(0,0,0,0.18);
  }
  .card-art {
    position: absolute;
    inset: 0;
    width: 1000px;
    height: 611px;
  }
  .card-text {
    position: absolute;
    color: var(--text-white);
    font-weight: 400;
    white-space: nowrap;
  }
  .brand-name {
    left: 56px;
    top: 62px;
    font-size: 50px;
    letter-spacing: 1px;
  }
  .contact-names {
    left: 60px;
    top: 232px;
    font-size: 38px;
  }
  .contact-details {
    left: 62px;
    top: 382px;
    font-size: 25px;
    line-height: 43px;
  }
  .website {
    left: 58px;
    top: 548px;
    font-size: 30px;
    letter-spacing: 0.5px;
  }
</style>
</head>
<body>
  <div class="business-card">
    <svg class="card-art" viewBox="0 0 1000 611" xmlns="http://www.w3.org/2000/svg">
      <defs>
        <linearGradient id="vehicle-photo-tones" x1="0" y1="0" x2="0" y2="1">
          <stop offset="0" stop-color="var(--photo-sky)"/>
          <stop offset="0.28" stop-color="var(--photo-trees)"/>
          <stop offset="0.5" stop-color="var(--photo-car)"/>
          <stop offset="0.72" stop-color="var(--photo-car)"/>
          <stop offset="1" stop-color="var(--photo-brick)"/>
        </linearGradient>
      </defs>
      <rect class="vehicle-photo" x="470" y="0" width="530" height="611"
            fill="url(#vehicle-photo-tones)" role="img"
            aria-label="Photo of a silver Pel luxury sedan parked on a brick driveway with trees behind"/>
      <path class="swoosh-grey" d="M500,0 H600 C545,90 540,330 560,611 H480 Z" fill="var(--swoosh-grey)"/>
      <path class="swoosh-white" d="M500,0 H575 C525,100 520,330 535,611 H480 Z" fill="var(--swoosh-white)"/>
      <path class="panel-charcoal" d="M0,0 H540 C505,110 500,330 512,611 H0 Z" fill="var(--card-charcoal)"/>
      <path class="band-grey" d="M0,522 H520 C525,555 530,585 540,611 H0 Z" fill="var(--band-grey)"/>
      <rect class="brand-rule" x="58" y="132" width="0" height="0" fill="none"/>
    </svg>

    <div class="card-text brand-name">BRISTEL QDF</div>
    <div class="card-text contact-names">Laurent &amp; Marisol</div>
    <div class="card-text contact-details">
      PO Box 287, Tarrowin WA 6311<br>
      Tel: 0427 381 594<br>
      Lic 7169/5804 | ABN 52 914 603 278
    </div>
    <div class="card-text website">www.BRISTELQDF.com.au</div>
  </div>
</body>
</html>
```